need 3 size package design

we need a package design for LED MINING LIGHT, there have 3size, which is for 1pcs, 20pcs, and 60pcs. L*W*H(1pcs 12.6*10.2*8.2 cm), (20pcs 41.2*27.1*21.5cm), (60 pcs 52*38.6*34.6 cm),The text on the package you can refer to the upload files.
The request for the design is: international, simple, noble and easy to printing.

For 20pcs and 60pcs, it is use for 20pcs and 60pcs of lights package box, so it just more simple than the 1pcs. it also can be not colorful for the 20pcs & 60pcs, but one color need to be the oxford color(the common box color).

Our company name is: plovek group co.,ltd, and website address is: www.plovek.com
our new LOGO file is also upload, thanks.
If ok, is there any possible to design a simple VI firstly, then to design the package box design, and we can raise the price for this project(if there have the nice design), thanks.

There don't need to put the mining headlight picture on the package, for there have 5 types different lamps use this one package. We upload the picture of the LED HEADLIGHT 1,2 picturesonly for refer to what's products will use this package, thank you.

We just upload a picture for refer to the text(20pcs and 60pcs), the company name can use plovek group or plovek group co.,ltd, please check the new upload file, thanks.

the 20 & 60pcs text refer to picture, also the color (background) is the oxfor color, so there only need two color just like the picture show for 20pcs & 60pcs package, thank you.

Target Market(s)

big trade company in the world.

Industry/Entity Type

Mining

Requirements
Must have
• our logo, and our website address

```html
<!DOCTYPE html>
<html lang="en">
<head>
<meta charset="utf-8">
<title>plovek LED Headlight – Box Dieline</title>
<link rel="stylesheet" href="https://fonts.googleapis.com/css2?family=Arimo:wght@400&display=swap">
<style>
  :root {
    --paper: #ffffff;
    --box-black: #000000;
    --fold-line: #ffffff;
    --text-white: #ffffff;
    --brand-grey: #7e868d;
    --brand-green: #8dc63f;
    --label-white: #ffffff;
  }
  * { margin: 0; padding: 0; box-sizing: border-box; }
  html, body {
    width: 1200px; height: 758px; overflow: hidden;
    background: var(--paper);
    font-family: "Arimo", Arial, sans-serif;
  }
  .dieline { position: relative; width: 1200px; height: 758px; }
  .dieline-art { position: absolute; inset: 0; }

  .copy { position: absolute; color: var(--text-white); font-size: 10.5px; line-height: 16px; white-space: nowrap; }
  .web { position: absolute; font-size: 10.5px; line-height: 12px; white-space: nowrap; }
  .web--green { color: var(--brand-green); }
  .web--white { color: var(--text-white); }

  .brand { position: absolute; display: flex; flex-direction: column; align-items: center; }
  .brand-mark { background: var(--brand-green); }
  .brand-name { color: var(--brand-grey); font-weight: 400; letter-spacing: 1px; line-height: 1; }

  .brand--front .brand-mark { width: 58px; height: 58px; margin-bottom: 22px; }
  .brand--front .brand-name { font-size: 56px; }

  .brand--side { flex-direction: row; }
  .brand--side .brand-mark { width: 24px; height: 24px; margin-right: 8px; }
  .brand--side .brand-name { font-size: 32px; }

  .label-blank { position: absolute; left: 370px; top: 410px; width: 117px; height: 55px; background: var(--label-white); }

  .top-panel { position: absolute; left: 540px; top: 100px; width: 277px; height: 172px; transform: rotate(180deg); }

  .spec-line { position: absolute; color: var(--text-white); font-size: 10.5px; line-height: 13px; white-space: pre; }
</style>
</head>
<body>
<main class="dieline">
  <svg class="dieline-art" width="1200" height="758" viewBox="0 0 1200 758" role="img" aria-label="Box dieline with dark background of blue, violet and red bokeh light orbs and lens flares">
    <defs>
      <radialGradient id="glow-blue" cx="0.5" cy="0.5" r="0.5">
        <stop offset="0" stop-color="#2a3ad0" stop-opacity="0.9"/>
        <stop offset="1" stop-color="#2a3ad0" stop-opacity="0"/>
      </radialGradient>
      <radialGradient id="glow-violet" cx="0.5" cy="0.5" r="0.5">
        <stop offset="0" stop-color="#7a2a9a" stop-opacity="0.8"/>
        <stop offset="1" stop-color="#7a2a9a" stop-opacity="0"/>
      </radialGradient>
      <radialGradient id="glow-red" cx="0.5" cy="0.5" r="0.5">
        <stop offset="0" stop-color="#8a1030" stop-opacity="0.8"/>
        <stop offset="1" stop-color="#8a1030" stop-opacity="0"/>
      </radialGradient>
      <radialGradient id="glow-white" cx="0.5" cy="0.5" r="0.5">
        <stop offset="0" stop-color="#ffffff" stop-opacity="0.9"/>
        <stop offset="0.3" stop-color="#9ad8ff" stop-opacity="0.4"/>
        <stop offset="1" stop-color="#9ad8ff" stop-opacity="0"/>
      </radialGradient>
      <clipPath id="box-shape">
        <path d="M80 272 H360 L395 140 H540 V45 H817 V140 H960 L995 272 V503 L1000 645 H848 L817 503 H540 V640 H360 V738 H90 L80 685 Z"/>
      </clipPath>
    </defs>

    <path class="box-outline" d="M80 272 H360 L395 140 H540 V45 H817 V140 H960 L995 272 V503 L1000 645 H848 L817 503 H540 V640 H360 V738 H90 L80 685 Z" fill="var(--box-black)" stroke="var(--box-black)" stroke-width="12" stroke-linejoin="miter"/>

    <g class="bokeh" clip-path="url(#box-shape)">
      <ellipse cx="470" cy="200" rx="170" ry="130" fill="url(#glow-blue)"/>
      <ellipse cx="760" cy="160" rx="110" ry="100" fill="url(#glow-blue)"/>
      <ellipse cx="720" cy="290" rx="120" ry="90" fill="url(#glow-violet)"/>
      <ellipse cx="530" cy="380" rx="110" ry="90" fill="url(#glow-red)"/>
      <ellipse cx="420" cy="520" rx="140" ry="150" fill="url(#glow-blue)"/>
      <ellipse cx="150" cy="450" rx="110" ry="100" fill="url(#glow-violet)"/>
      <ellipse cx="350" cy="640" rx="90" ry="90" fill="url(#glow-violet)"/>
      <ellipse cx="920" cy="470" rx="90" ry="80" fill="url(#glow-violet)"/>
      <ellipse cx="700" cy="520" rx="140" ry="40" fill="url(#glow-blue)"/>
      <ellipse cx="355" cy="270" rx="60" ry="60" fill="url(#glow-white)"/>
      <ellipse cx="535" cy="495" rx="60" ry="60" fill="url(#glow-white)"/>
      <rect x="80" y="266" width="560" height="6" fill="url(#glow-white)" opacity="0.6"/>
      <rect x="200" y="497" width="660" height="7" fill="url(#glow-white)" opacity="0.6"/>
    </g>

    <g class="fold-lines" fill="none" stroke="var(--fold-line)" stroke-width="1">
      <path d="M87 279 V683 L96 731 H353 V685 H87"/>
      <path d="M367 271 L400 147 H533 V272"/>
      <path d="M547 272 V100 L553 52 H804 L810 100 V272"/>
      <path d="M824 272 V147 H955 L988 272"/>
      <path d="M87 279 H988 V503 H87"/>
      <path d="M547 100 H810"/>
      <path d="M360 272 V640 M540 272 V503 M817 272 V503"/>
      <path d="M367 503 V633 H533 V503"/>
      <path d="M824 503 L852 638 H993 L988 503"/>
    </g>
  </svg>

  <!-- Front panel -->
  <p class="copy" style="left:102px; top:288px;">LED HEADLIGHT<br>Li-ion Battery</p>
  <div class="brand brand--front" style="left:104px; top:330px; width:220px;">
    <span class="brand-mark"></span>
    <span class="brand-name">plovek</span>
  </div>
  <p class="web web--green" style="left:175px; top:475px;">www.plovek.com</p>

  <!-- Side panel -->
  <div class="brand brand--side" style="left:370px; top:290px;">
    <span class="brand-mark"></span>
    <span class="brand-name">plovek</span>
  </div>
  <p class="copy" style="left:370px; top:329px;">LED HEADLIGHT<br>Li-ion Battery</p>
  <div class="label-blank"></div>
  <p class="web web--white" style="left:370px; top:475px;">www.plovek.com</p>

  <!-- Back panel -->
  <p class="copy" style="left:555px; top:288px;">LED HEADLIGHT<br>Li-ion Battery</p>
  <div class="brand brand--front" style="left:568px; top:330px; width:220px;">
    <span class="brand-mark"></span>
    <span class="brand-name">plovek</span>
  </div>
  <p class="web web--green" style="left:642px; top:475px;">www.plovek.com</p>

  <!-- Specification panel -->
  <p class="spec-line" style="left:830px; top:296px;">Input: AC110-240V</p>
  <p class="spec-line" style="left:858px; top:312px;">50～60Hz</p>
  <p class="spec-line" style="left:830px; top:343px;">Model: O PV2.5MA    O PV2.5MB</p>
  <p class="spec-line" style="left:862px; top:356px;">O PV3MA     O PV3MB</p>
  <p class="spec-line" style="left:862px; top:369px;">O PV4.5M-3W Lumora</p>
  <p class="spec-line" style="left:830px; top:401px;">Feature: Environmental friendly</p>
  <p class="spec-line" style="left:869px; top:414px;">Free maintenance</p>
  <p class="spec-line" style="left:869px; top:427px;">Long lifetime</p>
  <p class="web web--white" style="left:830px; top:475px;">www.plovek.com</p>

  <!-- Top lid (printed upside down) -->
  <div class="top-panel">
    <div class="brand brand--side" style="left:12px; top:16px;">
      <span class="brand-mark" style="width:34px;height:34px;"></span>
      <span class="brand-name" style="font-size:44px;">plovek</span>
    </div>
    <p class="copy" style="left:12px; top:72px;">LED HEADLIGHT<br>Li-ion Battery</p>
    <p class="web web--white" style="left:12px; top:146px;">www.plovek.com</p>
  </div>
</main>
</body>
</html>
```